Flyer/Broschürre für Ambulanter Betreuungsdienst
Zielgruppe
Ambulanter Betreuungsdienst,Dienstleistungen für Senioren und Menschen mit Beeinträchtigung
Nach Paragraph 43b 45a/b & 53b SGBXI
Unterstützung im Alltag:
-Begleitung zu Arztbesuchen,Therapien &Terminbegleitung aller Art,
-Hilfe beim Einkaufen & Besorgungen + Transport
-Unterstützung bei der Tagesstrukturierung & Organisation im Alltag
-Erinnerungsservice zb. Einahme von Medikamenten ggbf. Kontrolle
-Begleitung zu Sportveranstaltungen,Theater uvm.
für zuverlässige Sicherheit und Orientierung.
-Gemeinsames Spazieren gehen ( Bewegungsangebote)
- Lesen & Vorlesen
-Gemeinsames Kochen und geselschaft leisten beim essen.
-Unterstützung bei Terminplanungen,Hilfe bei der komunikation mit Medizinischen Personal.
Soziale Betreuung & Aktivierung:
-Geselschaft leisten,Gespräche führen ;
-Freizeitaktivitäten Planen & Durchführen
-Gemeinsames Lesen und Vorlesen
-Karten & Brettspiele spielen
-Malen & Basteln
-Briefe schreiben,Emails verfassen
-Gemeinsam alte interessen wecken und neue finden.
-Angehörige entlasten
-kommunikation & Informationsaustausch über Fortschritte und Bedürfnisse
-Betreuung & Aktivierung für Menschen mit Demenz
-Erinnerungspflege,Biografie Arbeit
-Individuelle Betreuung
-Kurz und Langzeit Betreuung
-Nachtpflege
-Bewegungsangebote
-Spiele spielen zb. Brett & Gemeinschsftsspiele
Dienstleistungen Haushaltsbereich
-Reinigung von Böden(Saugen & Wischen)
-Reinigung Küche und Bad
-Bett frisch Beziehen
-Fenster Reinigung (innen & außen)
-Haustiere versorgen (mit dem Hund spazieren gehen)
-Wäsche waschen
-Dekorieren
-uvm
Aufgabenstellung
Freundliches Design , vertrauenswürdiges Erscheinungsbild mit warmen Farben.
Firmenname ( Sonnwerk) logo sollte einen Sonnwerk darstellen.
Slogan Text:
Verlässlichkeit und Fürsorge mit Herz & Verstand.
Format soll handlich und nicht zu klein sein,damit Senioren es gut lesen bzw erkennen können.

```html
<!DOCTYPE html>
<html lang="de">
<head>
<meta charset="utf-8">
<title>Sonnwerk – Ambulanter Betreuungsdienst</title>
<link rel="stylesheet" href="https://fonts.googleapis.com/css2?family=Catamaran:wght@400;500;600;700&family=Montserrat:wght@400;500;600;700&family=Kalam:wght@700&display=swap">
<style>
:root{
  --blue:#2c5e9b;
  --blue-dark:#234f86;
  --orange:#c9641f;
  --brown:#763712;
  --ink:#1c1c1c;
  --white:#ffffff;
  --cream:#fbf4ea;
}
*{margin:0;padding:0;box-sizing:border-box}
html,body{width:836px;height:1200px;overflow:hidden;background:var(--white)}
body{position:relative;font-family:"Montserrat",sans-serif;color:var(--ink)}
.abs{position:absolute}

/* ---------- front page ---------- */
.front{position:absolute;left:0;top:0;width:836px;height:597px;overflow:hidden}
.front-scene{position:absolute;inset:0;
  background:
   radial-gradient(ellipse 300px 160px at 440px 330px,rgba(255,205,120,.85),transparent 70%),
   linear-gradient(180deg,#fdfcfa 0%,#fbf1e4 30%,#f3d3a3 50%,#c9a98c 65%,#d9c6b1 80%,#cfc0ae 100%)}
.hands{position:absolute;left:392px;top:306px;width:444px;height:227px;
  background:radial-gradient(ellipse 230px 100px at 240px 110px,#c67a4f 0%,#e3a37b 45%,rgba(240,190,140,0) 100%)}
.contact-heading{position:absolute;left:0;width:430px;top:40px;text-align:center;
  font-family:"Catamaran",sans-serif;font-weight:700;font-size:24px;line-height:29px;color:var(--blue)}
.contact-intro{position:absolute;left:0;width:430px;top:115px;text-align:center;
  font-family:"Catamaran",sans-serif;font-weight:400;font-size:16.5px;line-height:20px;color:var(--orange)}
.contact-card{position:absolute;left:42px;top:189px;width:350px;height:240px;border-radius:10px 10px 0 0;
  background:linear-gradient(180deg,rgba(255,255,255,.96) 30%,rgba(255,255,255,.75) 70%,rgba(255,255,255,0) 100%)}
.contact-card-title{height:66px;background:var(--blue);border-radius:10px 10px 0 0;color:var(--white);
  font-family:"Catamaran",sans-serif;font-weight:600;font-size:18.5px;line-height:22px;text-align:center;padding-top:11px}
.contact-row{position:absolute;left:26px;display:flex;align-items:center;gap:0}
.contact-row svg{width:22px;height:22px;fill:var(--blue);margin-right:20px}
.contact-row .label{font-weight:700;color:var(--ink)}
.contact-row .value{color:var(--blue);font-weight:500}
.row-phone{top:83px;font-size:19px}
.row-phone .value{font-family:"Catamaran",sans-serif;font-weight:500;font-size:21px}
.row-mail{top:128px;font-size:13.5px}
.row-web{top:159px;font-size:13.5px}
.row-address{top:191px;font-size:13.5px;align-items:flex-start}
.row-address .label{line-height:16px}
.seal{position:absolute;left:246px;top:387px;width:146px;height:146px;border-radius:50%;
  border:2px solid rgba(44,60,90,.55);background:rgba(255,255,255,.18)}

.brand-mark{position:absolute;left:587px;top:36px;width:84px;height:84px;border-radius:50%;
  border:5px solid #4d95d6;background:#fff}
.brand-name{position:absolute;left:436px;width:375px;top:118px;text-align:center;
  font-family:"Catamaran",sans-serif;font-weight:700;font-size:46px;line-height:54px;color:var(--blue)}
.brand-type{position:absolute;left:436px;width:375px;top:162px;text-align:center;
  font-family:"Catamaran",sans-serif;font-weight:600;font-size:24px;line-height:28px;color:var(--blue)}
.brand-audience{position:absolute;left:436px;width:375px;top:190px;text-align:center;
  font-family:"Catamaran",sans-serif;font-weight:400;font-size:16px;line-height:20px;color:var(--orange)}
.slogan{position:absolute;left:436px;width:375px;top:232px;text-align:center;
  font-family:"Kalam",cursive;font-weight:700;font-style:italic;font-size:24px;line-height:29px;color:var(--brown)}

.cta-band{position:absolute;left:0;width:836px;height:64px;background:var(--blue);color:var(--white);
  font-family:"Catamaran",sans-serif;font-weight:600;font-size:26px}
.cta-band span{position:absolute;top:50%;transform:translateY(-50%);white-space:nowrap}
.cta-front{top:533px}
.cta-back{top:1133px;height:67px}

/* ---------- inside page ---------- */
.inside{position:absolute;left:0;top:600px;width:836px;height:533px;overflow:hidden;
  background:linear-gradient(180deg,#ffffff 0%,#fdf8f1 40%,#f6ecdf 75%,#ece6e4 100%)}
.inside-header{position:absolute;left:0;top:0;width:836px;height:112px}
.inside-claim{position:absolute;left:0;width:434px;top:28px;text-align:center;color:var(--white);
  font-family:"Catamaran",sans-serif;font-weight:600;font-size:24px;line-height:29px}
.services-title{position:absolute;left:430px;width:380px;top:25px;text-align:center;color:var(--white);
  font-family:"Catamaran",sans-serif;font-weight:600;font-size:25px;letter-spacing:.5px}
.intro{position:absolute;left:36px;width:370px;top:120px;text-align:center;
  font-family:"Montserrat",sans-serif;font-weight:400;font-size:15.4px;line-height:19px;color:var(--orange)}
.intro b{font-weight:700}
.benefits{position:absolute;left:78px;top:224px;width:283px;height:151px;border-radius:8px;
  background:rgba(255,255,255,.8);padding:6px 14px 0 12px}
.benefit{display:flex;align-items:center;height:24.5px;border-bottom:1px solid #e4ddd5;font-size:11.4px}
.benefit:last-child{border-bottom:none;height:36px;align-items:center}
.benefit svg{width:21px;height:21px;flex:none;margin-right:9px}
.benefit b{font-weight:700}

.section-title{position:absolute;font-family:"Catamaran",sans-serif;font-weight:700;font-size:21px;line-height:24px;color:var(--blue);white-space:nowrap}
.service-list{position:absolute;list-style:none;font-size:9.5px;line-height:11.75px}
.service-list li{position:relative;padding-left:18px}
.service-list li::before{content:"";position:absolute;left:1px;top:5px;width:3px;height:3px;background:var(--ink)}
.service-list b{font-weight:700}

.photo{position:absolute;border-radius:40% 40% 30% 30%}
.photo-alltag{left:405px;top:113px;width:110px;height:118px;background:radial-gradient(ellipse at 50% 45%,#d9e4ef 0%,#e8e2dc 55%,rgba(250,245,238,0) 75%)}
.photo-sozial{left:669px;top:223px;width:162px;height:165px;background:radial-gradient(ellipse at 50% 50%,#e6ddd0 0%,#efe9e2 55%,rgba(250,245,238,0) 75%)}
.photo-haushalt{left:332px;top:372px;width:175px;height:159px;background:radial-gradient(ellipse at 50% 50%,#b9d6ea 0%,#e7ddd4 55%,rgba(245,240,236,0) 75%)}
</style>
</head>
<body>

<section class="front">
  <div class="front-scene" role="img" aria-label="Warmes Abendlicht über einer Blumenwiese"></div>
  <div class="hands" role="img" aria-label="Junge Hand hält die Hand eines älteren Menschen"></div>

  <h2 class="contact-heading">Wir beraten Sie gerne<br>persönlich &amp; unverbindlich</h2>
  <p class="contact-intro">Gemeinsam finden wir die passende<br>Unterstützung für Ihre individuelle<br>Situation.</p>

  <div class="contact-card">
    <div class="contact-card-title">Sonnwerk – Ambulanter<br>Betreuungsdienst</div>
    <div class="contact-row row-phone">
      <svg viewBox="0 0 24 24"><path d="M6.6 10.8a15.1 15.1 0 0 0 6.6 6.6l2.2-2.2c.3-.3.7-.4 1-.2 1.1.4 2.3.6 3.6.6.6 0 1 .4 1 1V20c0 .6-.4 1-1 1A17 17 0 0 1 3 4c0-.6.4-1 1-1h3.5c.6 0 1 .4 1 1 0 1.3.2 2.5.6 3.6.1.3 0 .7-.2 1z"/></svg>
      <span class="label">Telefon:&nbsp;</span><span class="value">0XXX / XXXXXXX</span>
    </div>
    <div class="contact-row row-mail">
      <svg viewBox="0 0 24 24"><path d="M2 5h20v3l-10 6L2 8zM2 10l10 6 10-6v9H2z"/></svg>
      <span class="label">E-Mail:&nbsp;</span><span class="value">info@sonnwerk-betreuung.de</span>
    </div>
    <div class="contact-row row-web">
      <svg viewBox="0 0 24 24"><path d="M12 2a10 10 0 1 0 0 20 10 10 0 0 0 0-20zm0 2c1 0 2.3 2 2.8 5H9.2C9.7 6 11 4 12 4zM4.4 10h3.7a20 20 0 0 0 0 4H4.4a8 8 0 0 1 0-4zm5 0h5.2a18 18 0 0 1 0 4H9.4a18 18 0 0 1 0-4zm6.5 0h3.7a8 8 0 0 1 0 4h-3.7a20 20 0 0 0 0-4zM9.2 15h5.6c-.5 3-1.8 5-2.8 5s-2.3-2-2.8-5z"/></svg>
      <span class="label">Web:&nbsp;</span><span class="value">www.sonnwerk-betreuung.de</span>
    </div>
    <div class="contact-row row-address">
      <svg viewBox="0 0 24 24"><path d="M12 2a7 7 0 0 0-7 7c0 5 7 13 7 13s7-8 7-13a7 7 0 0 0-7-7zm0 9.5A2.5 2.5 0 1 1 12 6.5a2.5 2.5 0 0 1 0 5z"/></svg>
      <span class="label">Straße &amp; Hausnummer<br>PLZ Ort</span>
    </div>
  </div>

  <div class="seal" role="img" aria-label="Siegel für anerkannte Betreuungsleistungen"></div>

  <div class="brand-mark" aria-hidden="true"></div>
  <h1 class="brand-name">Sonnwerk</h1>
  <p class="brand-type">Ambulanter Betreuungsdienst</p>
  <p class="brand-audience">Für Senioren &amp; Menschen mit Beeinträchtigung</p>
  <p class="slogan">Verlässlichkeit und Fürsorge<br>mit Herz &amp; Verstand</p>
</section>

<div class="cta-band cta-front">
  <span style="left:41px">Beratungstermin vereinbaren!</span>
  <span style="left:482px">Telefon: 0XXX / XXXXXXX</span>
</div>

<section class="inside">
  <svg class="inside-header" viewBox="0 0 836 112" preserveAspectRatio="none" aria-hidden="true">
    <polygon points="0,0 836,0 836,56 0,112" fill="#2c5e9b"/>
  </svg>
  <h2 class="inside-claim">Für ein selbstbestimmtes<br>Leben im eigenen Zuhause</h2>
  <h2 class="services-title">UNSERE LEISTUNGEN</h2>

  <p class="intro">Wir unterstützen Senioren und Menschen mit Beeinträchtigung im Alltag – <b>zuverlässig, respektvoll und individuell</b>. Unser Ziel ist es, Lebensqualität zu erhalten, <b>Angehörige zu entlasten</b> und soziale Teilhabe zu ermöglichen.</p>

  <div class="benefits">
    <div class="benefit"><svg viewBox="0 0 24 24"><circle cx="8" cy="6" r="3.5" fill="#c9641f"/><path d="M2 20c0-5 3-8 6-8s6 3 6 8z" fill="#c9641f"/><circle cx="16" cy="10" r="3" fill="#2c5e9b"/><path d="M11 21c0-4 2-6 5-6s5 2 5 6z" fill="#2c5e9b"/></svg><span><b>Persönliche &amp; individuelle Betreuung</b></span></div>
    <div class="benefit"><svg viewBox="0 0 24 24"><rect x="4" y="2" width="13" height="19" rx="1" fill="#2c5e9b"/><path d="M7 7h7M7 10h7M7 13h5" stroke="#fff" stroke-width="1.4"/><circle cx="18" cy="18" r="4" fill="#c9641f"/></svg><span>Anerkannte Leistungen nach <b>SGB XI</b></span></div>
    <div class="benefit"><svg viewBox="0 0 24 24"><path d="M1 12l5-3 6 2 5-2 6 3-6 4h-6z" fill="#2c5e9b"/><path d="M9 11l4-2 5 1-4 4z" fill="#c9641f"/></svg><span><b>Zuverlässige Begleitung</b> im Alltag</span></div>
    <div class="benefit"><svg viewBox="0 0 24 24"><path d="M12 14s-6-3.5-6-7.5A3 3 0 0 1 12 5a3 3 0 0 1 6 1.5C18 10.5 12 14 12 14z" fill="#c9641f"/><path d="M2 15c3 0 5 3 10 3s7-2 10-4v3c-3 2-5 4-10 4S5 19 2 19z" fill="#2c5e9b"/></svg><span><b>Entlastung</b> für Angehörige</span></div>
    <div class="benefit"><svg viewBox="0 0 24 24"><circle cx="11" cy="6" r="4" fill="#c9641f"/><path d="M3 22c0-6 4-9 8-9s8 3 8 9z" fill="#2c5e9b"/><circle cx="18" cy="18" r="3.5" fill="#c9641f"/></svg><span><b>Herzliche &amp; qualifizierte</b> Betreuungs-<br>kräfte</span></div>
  </div>

  <div class="photo photo-alltag" role="img" aria-label="Foto: Betreuerin im Gespräch mit einer Seniorin"></div>
  <h3 class="section-title" style="left:538px;top:83px">Unterstützung im Alltag</h3>
  <ul class="service-list" style="left:520px;top:112px;width:300px">
    <li><b>Begleitung</b> zu Arzt-, Therapie- &amp; Behördenterminen</li>
    <li>Hilfe beim <b>Einkaufen &amp; Besorgungen</b> inkl. Transport</li>
    <li>Unterstützung bei <b>Tagesstruktur &amp; Alltagsorganisation</b></li>
    <li><b>Erinnerungsservice</b> (z. B. Medikamenteneinnahme)</li>
    <li>Begleitung zu <b>Freizeit- &amp; Kulturveranstaltungen</b></li>
    <li>Gemeinsames Spazierengehen &amp; <b>Bewegungsangebote</b></li>
    <li><b>Lesen &amp; Vorlesen</b></li>
    <li>Gemeinsames Kochen &amp; <b>Gesellschaft</b> beim Essen</li>
    <li>Unterstützung bei <b>Terminplanung &amp; Kommunikation</b><br>mit medizinischem Personal</li>
  </ul>

  <div class="photo photo-sozial" role="img" aria-label="Foto: Pflegerin stützt einen älteren Herrn beim Gehen"></div>
  <h3 class="section-title" style="left:434px;top:243px">Soziale Betreuung &amp; Aktivierung</h3>
  <ul class="service-list" style="left:437px;top:273px;width:240px">
    <li><b>Gesellschaft leisten</b> &amp; Gespräche führen</li>
    <li>Freizeitaktivitäten planen &amp; durchführen</li>
    <li><b>Gemeinsames</b> Lesen &amp; Vorlesen</li>
    <li>Karten- &amp; Brettspiele</li>
    <li>Malen, Basteln &amp; <b>kreative Angebote</b></li>
    <li>Briefe schreiben &amp; E-Mails verfassen</li>
    <li>Alte Interessen wecken &amp; neue entdecken</li>
    <li><b>Angehörige entlasten</b></li>
    <li>Regelmäßiger Informationsaustausch mit<br>Angehörigen</li>
  </ul>

  <div class="photo photo-haushalt" role="img" aria-label="Foto: Betreuerin umarmt eine lächelnde Seniorin"></div>
  <h3 class="section-title" style="left:45px;top:389px">Dienstleistungen im Haushalt</h3>
  <ul class="service-list" style="left:46px;top:419px;width:280px">
    <li><b>Bodenreinigung</b> (Saugen &amp; Wischen)</li>
    <li>Reinigung von <b>Küche &amp; Bad</b></li>
    <li>Betten frisch beziehen</li>
    <li><b>Fensterreinigung</b> (innen &amp; außen)</li>
    <li><b>Haustierbetreuung</b> (z. B. Hund ausführen)</li>
    <li><b>Wäsche</b> waschen</li>
    <li><b>Dekorieren</b></li>
    <li>… und <b>vieles mehr</b></li>
  </ul>

  <h3 class="section-title" style="left:587px;top:408px">Betreuung bei Demenz</h3>
  <ul class="service-list" style="left:578px;top:444px;width:250px">
    <li><b>Individuelle Betreuung</b></li>
    <li>Erinnerungspflege &amp; Biografiearbeit</li>
    <li>Kurz- &amp; Langzeitbetreuung</li>
    <li>Nachtpflege</li>
    <li>Bewegungsangebote</li>
    <li>Spiele &amp; gemeinschaftliche Aktivitäten</li>
  </ul>
</section>

<div class="cta-band cta-back">
  <span style="left:47px">Beratungstermin vereinbaren!</span>
  <span style="left:476px">Telefon: 0XXX / XXXXXXX</span>
</div>

</body>
</html>
```